Business card design for online Mandarin Learning School

We need a business card design for our online language learning school called "Maple Bridge Online for Mandarin Learning". Our existing website is https://www.maplebridgeonline.com
We have our logo already. We would like to see our business card design that can make our online teaching services to be innovative, young, energetic and fun to learn. Prefer to have a certain level of color matching with our website. Apart from "Maple Bridge Online", need to specifically state "for Mandarin Learning" as well on the business card.

```html
<!DOCTYPE html>
<html lang="en">
<head>
<meta charset="utf-8">
<title>Maple Bridge Online for Mandarin Learning – Business Card</title>
<link rel="stylesheet" href="https://fonts.googleapis.com/css2?family=Marcellus&family=Tinos:wght@400;700&display=swap">
<style>
  :root {
    --backdrop: #d3d3d3;
    --card: #ffffff;
    --teal: #1cbfcb;
    --teal-deep: #14a9b5;
    --ink: #3b3b3b;
    --grey: #8f8f8f;
    --coral: #ea6f66;
    --rule: #a9a9a9;
  }
  * { box-sizing: border-box; margin: 0; padding: 0; }
  html, body { width: 1200px; height: 1200px; overflow: hidden; }
  body {
    background: var(--backdrop);
    position: relative;
    font-family: "Tinos", "Times New Roman", serif;
  }
  .card {
    position: absolute;
    left: 250px;
    width: 700px;
    height: 400px;
    background: var(--card);
    overflow: hidden;
  }
  .card--brand { top: 150px; }
  .card--contact { top: 650px; }

  /* Brand side */
  .brand-band {
    position: absolute;
    left: 0; right: 0; top: 140px; bottom: 0;
    background: linear-gradient(180deg, var(--teal), var(--teal-deep));
  }
  .brand-dot {
    position: absolute;
    left: 480px; top: 52px;
    width: 56px; height: 56px;
    border-radius: 50%;
    background: var(--coral);
  }
  .brand-name {
    position: absolute;
    left: 40px; right: 40px; top: 160px;
    font-family: "Marcellus", serif;
    font-size: 50px;
    font-weight: 400;
    letter-spacing: 2px;
    color: var(--ink);
    text-transform: uppercase;
    text-align: center;
    white-space: nowrap;
  }
  .brand-tagline {
    position: absolute;
    left: 40px; right: 40px; top: 226px;
    font-family: "Marcellus", serif;
    font-size: 22px;
    letter-spacing: 3px;
    color: var(--ink);
    text-transform: uppercase;
    text-align: center;
  }
  .brand-rule {
    position: absolute;
    left: 60px; right: 60px; top: 268px;
    height: 2px;
    background: var(--ink);
  }
  .brand-url {
    position: absolute;
    left: 40px; right: 40px; top: 290px;
    font-family: "Marcellus", serif;
    font-size: 27px;
    letter-spacing: 2px;
    color: var(--ink);
    text-transform: uppercase;
    text-align: center;
  }

  /* Contact side */
  .person {
    position: absolute;
    left: 48px; top: 118px;
  }
  .person-name {
    font-size: 26px;
    font-weight: 700;
    color: var(--teal);
    text-transform: uppercase;
    letter-spacing: 0.5px;
  }
  .person-role {
    font-size: 15px;
    color: var(--grey);
    text-transform: uppercase;
    letter-spacing: 1px;
    margin-top: 2px;
  }
  .wordmark {
    position: absolute;
    left: 300px; top: 56px;
    display: flex;
    align-items: center;
    gap: 14px;
  }
  .wordmark-dot {
    width: 30px; height: 30px;
    border-radius: 50%;
    background: var(--coral);
  }
  .wordmark-name {
    font-family: "Marcellus", serif;
    font-size: 30px;
    letter-spacing: 2px;
    color: var(--teal);
    text-transform: uppercase;
  }
  .wordmark-tagline {
    position: absolute;
    left: 344px; top: 98px;
    font-family: "Marcellus", serif;
    font-size: 15px;
    letter-spacing: 2px;
    color: var(--grey);
    text-transform: uppercase;
  }
  .divider {
    position: absolute;
    left: 318px; top: 160px;
    width: 1px; height: 130px;
    background: var(--rule);
  }
  .contact-list {
    position: absolute;
    left: 346px; top: 168px;
    list-style: none;
  }
  .contact-item {
    display: flex;
    align-items: center;
    gap: 10px;
    font-size: 19px;
    line-height: 28px;
    color: #1e1e1e;
  }
  .contact-icon { width: 15px; height: 15px; flex: none; }
</style>
</head>
<body>

<section class="card card--brand" aria-label="Card back">
  <div class="brand-band"></div>
  <div class="brand-dot"></div>
  <h1 class="brand-name">Maple Bridge Online</h1>
  <p class="brand-tagline">for Mandarin Learning</p>
  <div class="brand-rule"></div>
  <p class="brand-url">www.maplebridgeonline.com</p>
</section>

<section class="card card--contact" aria-label="Card front">
  <div class="person">
    <p class="person-name">Lena Ortiz</p>
    <p class="person-role">Director</p>
  </div>

  <div class="wordmark">
    <span class="wordmark-dot"></span>
    <span class="wordmark-name">Maple Bridge</span>
  </div>
  <p class="wordmark-tagline">for Mandarin Learning</p>

  <div class="divider"></div>

  <ul class="contact-list">
    <li class="contact-item">
      <svg class="contact-icon" viewBox="0 0 16 16"><circle cx="8" cy="8" r="8" fill="#1cbfcb"/><path d="M5 4.5l1.6-.4 1 2.2-1 .8a5 5 0 0 0 2.3 2.3l.8-1 2.2 1-.4 1.6c-3.4.3-6.8-3.1-6.5-6.5z" fill="#fff"/></svg>
      +8801712003344
    </li>
    <li class="contact-item">
      <svg class="contact-icon" viewBox="0 0 16 16"><rect x="1" y="3" width="14" height="10" rx="1" fill="#1cbfcb"/><path d="M1.5 4l6.5 5 6.5-5" stroke="#fff" stroke-width="1.4" fill="none"/></svg>
      lenaortiz@mail.com
    </li>
    <li class="contact-item">
      <svg class="contact-icon" viewBox="0 0 16 16"><circle cx="8" cy="8" r="7" fill="#1cbfcb"/><path d="M1 8h14M8 1c-3 3-3 11 0 14M8 1c3 3 3 11 0 14" stroke="#fff" stroke-width="1" fill="none"/></svg>
      www.lenaortizweb.com
    </li>
    <li class="contact-item">
      <svg class="contact-icon" viewBox="0 0 16 16"><rect x="1" y="1" width="14" height="14" rx="2" fill="#1cbfcb"/></svg>
      www.lenaortiz.page/connect56
    </li>
  </ul>
</section>

</body>
</html>
```